Business Cards and Logo

KWM - Personal Injury Attorneys is the name of the firm.
We are personal injury lawyers. We want a crisp, modern and impactful design.
Color schemes are white, matte black and light grey OR white, matte black and red OR white, matte black and a nice blue or yellow.
For logo - we don’t want typical logos like scales of justice or a hammer. We want a general design with the KWM letters.
Target Market(s)
People who need attorneys.
Industry/Entity Type
Law Firm
Contact Information for Business Card
Back side: text: Los Angeles - Santa Ana - San Diego - San Francisco
Front side
Name of firm and logo.
Marco Feltrovski
812 W. Colter Ave. 4th Floor
Glendale, CA 91207
(818)555-0172 (c)
(818)555-0194 (o)
Marco@fieldcounselwest.example
Logo Text
KWM
Font styles to use
Other font styles liked:
- Musk - regular. Military - regular. Moonglade. Future. Or similar fonts.
Requirements
Must have
- See above. Nothing else to provide.
- KWM - Personal Injury Attorneys is the name of the firm.
- We are personal injury lawyers. We want a crisp, modern and impactful design.
- Color schemes are white, matte black and light grey OR white, matte black and red OR white, matte black and a nice blue or yellow.
- For logo - we don’t want typical logos like scales of justice or a hammer. We want a general design with the KWM letters.
Nice to have
- See above - nothing else to provide.
Should not have

```html
<!DOCTYPE html>
<html lang="en">
<head>
<meta charset="utf-8">
<title>KWM - Personal Injury Attorneys — Business Cards</title>
<link rel="stylesheet" href="https://fonts.googleapis.com/css2?family=Lato:wght@400;700;900&family=Montserrat:wght@400;500&display=swap">
<style>
  :root {
    --bg: #e4e4e6;
    --blue: #3276b6;
    --blue-light: #86c6e6;
    --white: #ffffff;
    --grey-text: #7c7c80;
    --shadow: rgba(0, 0, 0, 0.18);
  }
  * { box-sizing: border-box; margin: 0; padding: 0; }
  html, body {
    width: 1200px; height: 900px; overflow: hidden;
    background: var(--bg);
    font-family: "Lato", Arial, sans-serif;
  }
  .stage { position: relative; width: 1200px; height: 900px; }
  .card {
    position: absolute; top: 301px;
    width: 520px; height: 298px;
    border-radius: 22px; overflow: hidden;
    box-shadow: 0 10px 24px var(--shadow);
  }
  /* Back */
  .card-back { left: 50px; background: var(--blue); color: var(--white); }
  .card-back .wordmark {
    position: absolute; left: 0; right: 0; top: 92px;
    text-align: center;
    font-family: "Montserrat", sans-serif; font-weight: 400;
    font-size: 78px; letter-spacing: 6px; line-height: 1;
  }
  .card-back .cities {
    position: absolute; left: 0; right: 0; bottom: 34px;
    text-align: center; font-size: 13px; letter-spacing: 1.2px;
    font-weight: 400; text-transform: uppercase;
  }
  /* Front */
  .card-front { left: 630px; background: var(--white); }
  .card-front .accent { position: absolute; inset: 0; }
  .brand {
    position: absolute; left: 236px; top: 28px;
    display: flex; align-items: center; gap: 12px;
  }
  .brand .wordmark {
    font-family: "Montserrat", sans-serif; font-weight: 400;
    font-size: 50px; letter-spacing: 3px; color: var(--blue); line-height: 1;
  }
  .brand .divider { width: 1px; height: 54px; background: var(--grey-text); opacity: .6; }
  .brand .tagline { display: flex; flex-direction: column; line-height: 1; text-transform: uppercase; }
  .tagline .t1 { font-size: 14px; color: var(--blue); font-weight: 400; letter-spacing: 1px; }
  .tagline .t2 { font-size: 23px; color: var(--blue); font-weight: 900; letter-spacing: .5px; }
  .tagline .t3 { font-size: 12px; color: var(--blue-light); font-weight: 700; letter-spacing: 1px; }
  .contact { position: absolute; left: 262px; top: 122px; color: var(--grey-text); }
  .contact .name {
    font-size: 19px; font-weight: 900; color: var(--blue);
    text-transform: uppercase; letter-spacing: .5px; margin-bottom: 8px;
  }
  .contact .line { display: flex; align-items: center; gap: 6px; font-size: 15px; line-height: 19px; }
  .contact .line svg { width: 12px; height: 12px; flex: none; }
  .contact .address { margin-top: 6px; font-size: 15px; line-height: 19px; }
</style>
</head>
<body>
<main class="stage">
  <section class="card card-back" aria-label="Business card back">
    <div class="wordmark">KWM</div>
    <p class="cities">Los Angeles - Santa Ana - San Diego - San Francisco</p>
  </section>

  <section class="card card-front" aria-label="Business card front">
    <svg class="accent" viewBox="0 0 520 298" preserveAspectRatio="none" aria-hidden="true">
      <path d="M0 70 H150 Q196 70 204 118 L228 298 H0 Z" fill="var(--blue)"/>
      <path d="M150 70 Q196 70 204 118 L228 298" fill="none" stroke="var(--blue-light)" stroke-width="6"/>
    </svg>

    <div class="brand">
      <span class="wordmark">KWM</span>
      <span class="divider"></span>
      <span class="tagline">
        <span class="t1">Personal</span>
        <span class="t2">Injury</span>
        <span class="t3">Attorneys</span>
      </span>
    </div>

    <div class="contact">
      <p class="name">Marco Feltrovski</p>
      <p class="line">
        <svg viewBox="0 0 12 12"><rect x="3" y="0.5" width="6" height="11" rx="1.2" fill="none" stroke="var(--blue)" stroke-width="1.2"/><circle cx="6" cy="9.6" r=".7" fill="var(--blue)"/></svg>
        (818)555-0172
      </p>
      <p class="line">
        <svg viewBox="0 0 12 12"><path d="M1 4 Q6 0 11 4 L9.5 5.5 L8 4.5 L4 4.5 L2.5 5.5 Z" fill="var(--blue)"/><rect x="2.5" y="6" width="7" height="5" rx="1" fill="var(--blue)"/></svg>
        (818)555-0194
      </p>
      <p class="line">
        <svg viewBox="0 0 12 12"><rect x="0.5" y="2.5" width="11" height="7.5" fill="var(--blue)"/><path d="M0.5 2.5 L6 7 L11.5 2.5" fill="none" stroke="var(--white)" stroke-width="1"/></svg>
        Marco@fieldcounselwest.example
      </p>
      <p class="address">812 W. Colter Ave. 4th Floor<br>Glendale, CA 91207</p>
    </div>
  </section>
</main>
</body>
</html>
```